Lift Her Forward, 2019 Save The Date

Please develop a save the date flyer our 4th Annual Lift Her Forward and See Her Rise! This event is focused on maintaining participation and appreciation for women in the design and construction industry.

This unique Forum provides a venue to engage everyone from executives to those just beginning their careers with active, hands-on sessions and vibrant networking with the best and brightest in the A/E/C industry. In our usual Q-TarVM Forum style, Keynotes become table participants and table participants become presenters, encouraging participants to assimilate what they are learning. Join local, state and national leaders and subject matter experts as we candidly explore and address the issues affecting women in our industry.

Industry/Entity Type

Construction

Font styles to use
Sans Serif

Requirements
Must have
• This is a save the date, Must have:
• Q-TarVM Logo
• Title: 4th Annual Lift Her Forward and See Her Rise!
• Date: January 25, 2019
• Location: Harbor Crest Resort and Spa, San Marcos, TX
Nice to have
• A header that can easily be pulled to add to other marketing materials and for use across other platforms (web, etc.).

```html
<!DOCTYPE html>
<html lang="en">
<head>
<meta charset="utf-8">
<title>Q-TarVM — Save The Date 2019</title>
<link href="https://fonts.googleapis.com/css2?family=Oswald:wght@400;500;600&family=Montserrat:wght@500;600&display=swap" rel="stylesheet">
<style>
  :root {
    --page-bg: #ffffff;
    --flyer-bg: #ececec;
    --brand-blue: #2f55a8;
    --brand-blue-dark: #1d3a86;
    --brand-green: #7aa62b;
    --ink: #4a4a4a;
    --ink-soft: #555555;
    --board: #f4f4f4;
    --box-line: #9a9a9a;
    --footer: #555555;
    --white: #ffffff;
    --photo-top: #e4e1de;
    --photo-mid: #d9cfc6;
    --photo-low: #f1f1f1;
    --photo-frame: #c9c4bf;
  }
  * { margin: 0; padding: 0; box-sizing: border-box; }
  html, body { width: 1200px; height: 1200px; overflow: hidden; background: var(--page-bg); }
  .flyer {
    position: absolute; left: 259px; top: 118px;
    width: 682px; height: 963px;
    background: linear-gradient(180deg, #eeeeee 0%, #e6e6e6 60%, #dadada 100%);
    overflow: hidden;
    font-family: "Montserrat", sans-serif;
  }
  .photo-area {
    position: absolute; left: 60px; top: 208px; width: 562px; height: 330px;
    border: 1px solid var(--photo-frame); border-radius: 6px;
    background: linear-gradient(180deg, var(--photo-top) 0%, var(--photo-mid) 45%, var(--photo-low) 100%);
  }
  .header { position: absolute; left: 0; top: 0; width: 682px; height: 190px; }
  .logo-mark {
    position: absolute; left: 163px; top: 60px; width: 108px; height: 108px;
    border-radius: 50%; background: var(--brand-blue);
  }
  .logo-name {
    position: absolute; left: 300px; top: 66px;
    font-family: "Montserrat", sans-serif; font-weight: 500;
    font-size: 52px; color: var(--ink-soft); letter-spacing: -1px; line-height: 1;
  }
  .logo-rule { position: absolute; left: 301px; top: 127px; width: 237px; height: 2px; background: var(--ink-soft); }
  .logo-tagline {
    position: absolute; left: 301px; top: 138px;
    font-family: "Oswald", sans-serif; font-weight: 400; font-size: 13px;
    color: var(--brand-green); white-space: nowrap;
  }
  .board {
    position: absolute; left: 41px; top: 510px; width: 601px; height: 404px;
    background: var(--board);
  }
  .banner {
    position: absolute; left: 113px; top: 522px; width: 456px; height: 100px;
    background: var(--brand-blue); border-radius: 8px;
    box-shadow: 0 10px 14px -8px rgba(0,0,0,.35);
    display: flex; align-items: center; justify-content: center;
    font-family: "Oswald", sans-serif; font-weight: 600; font-size: 66px;
    color: var(--white); letter-spacing: 0.5px;
  }
  .event-title {
    position: absolute; left: 41px; width: 601px; top: 652px; text-align: center;
    font-family: "Oswald", sans-serif; font-weight: 600; font-size: 56px;
    color: var(--brand-green); line-height: 1; letter-spacing: 0.5px;
  }
  .event-subtitle {
    position: absolute; left: 41px; width: 601px; top: 714px; text-align: center;
    font-weight: 600; font-size: 26px; color: var(--ink); letter-spacing: 0.8px;
  }
  .info-box {
    position: absolute; top: 794px; height: 92px;
    border: 1px solid var(--box-line); border-radius: 5px; background: var(--board);
    display: flex; align-items: center; justify-content: center; text-align: center;
    font-family: "Oswald", sans-serif; color: var(--ink);
  }
  .info-date { left: 54px; width: 256px; padding-top: 18px; font-size: 38px; }
  .info-date .year { color: var(--brand-blue-dark); }
  .info-place { left: 350px; width: 277px; padding-top: 20px; font-size: 21px; line-height: 1.25; }
  .info-icon { position: absolute; width: 58px; height: 58px; top: 761px; }
  .icon-date { left: 153px; }
  .icon-place { left: 459px; }
  .footer {
    position: absolute; left: 0; top: 902px; width: 682px; height: 61px;
    background: var(--footer);
    display: flex; align-items: center; justify-content: center; padding-top: 22px;
    color: var(--white); font-weight: 500; font-size: 18px; letter-spacing: 2.5px;
    z-index: 0;
  }
  .board, .banner, .event-title, .event-subtitle, .info-box, .info-icon { z-index: 1; }
</style>
</head>
<body>
  <main class="flyer">
    <header class="header">
      <div class="logo-mark"></div>
      <div class="logo-name">Q-TarVM</div>
      <div class="logo-rule"></div>
      <div class="logo-tagline">Quorum for Teamwork in Vital Megabuilds</div>
    </header>

    <div class="photo-area" role="img" aria-label="Photo of two smiling women in white t-shirts pointing down at the sign they hold"></div>

    <footer class="footer">www.q-tarvm.org</footer>

    <section class="board"></section>
    <div class="banner">SAVE THE DATE</div>
    <h1 class="event-title">4TH ANNUAL LIFT HER</h1>
    <p class="event-subtitle">Forward &amp; See Her Rise!</p>

    <div class="info-box info-date">January 25,&nbsp;<span class="year">2019</span></div>
    <svg class="info-icon icon-date" viewBox="0 0 58 58" aria-hidden="true">
      <circle cx="29" cy="29" r="28" fill="#7aa62b"/>
      <circle cx="29" cy="31" r="26" fill="#ffffff"/>
      <circle cx="29" cy="31" r="22" fill="#1d3a86"/>
      <rect x="17" y="21" width="24" height="20" rx="2" fill="none" stroke="#fff" stroke-width="2"/>
      <line x1="17" y1="26" x2="41" y2="26" stroke="#fff" stroke-width="2"/>
      <line x1="22" y1="18" x2="22" y2="23" stroke="#fff" stroke-width="2"/>
      <line x1="36" y1="18" x2="36" y2="23" stroke="#fff" stroke-width="2"/>
      <g fill="#fff">
        <rect x="20" y="29" width="3" height="3"/><rect x="25" y="29" width="3" height="3"/><rect x="30" y="29" width="3" height="3"/><rect x="35" y="29" width="3" height="3"/>
        <rect x="20" y="34" width="3" height="3"/><rect x="25" y="34" width="3" height="3"/><rect x="30" y="34" width="3" height="3"/>
      </g>
    </svg>

    <div class="info-box info-place">Harbor Crest Resort &amp; Spa,<br>San Marcos, TX</div>
    <svg class="info-icon icon-place" viewBox="0 0 58 58" aria-hidden="true">
      <circle cx="29" cy="29" r="28" fill="#7aa62b"/>
      <circle cx="29" cy="31" r="26" fill="#ffffff"/>
      <circle cx="29" cy="31" r="22" fill="#1d3a86"/>
      <path d="M29 42 C23 34 21 30 21 26 a8 8 0 0 1 16 0 c0 4 -2 8 -8 16z" fill="none" stroke="#fff" stroke-width="2"/>
      <circle cx="29" cy="26" r="3" fill="none" stroke="#fff" stroke-width="2"/>
      <ellipse cx="29" cy="43" rx="9" ry="2.5" fill="none" stroke="#fff" stroke-width="1.5"/>
    </svg>
  </main>
</body>
</html>
```